Revamp Website To A More Modern Up To Date Design Concepts

I am looking for a renewed look for my website.

Keep in mind that my business is B2B.

Please use and include all current content, text and imagery (you can adjust the imagery to fit your designs) and all current modules, features, videos, calls to action buttons, etc. Please do not omit anything from the current homepage. I prefer to see all my content as it is on my current site on the new design too so I can really invision my new site...so please do not use lipsum lorem text filler anywhere.

I am looking for an impressive looking and engaging high converting homepage.

Please be sure to keep all elements, links in header and footer etc. already on my current homepage at www.brightlanepromoworks.biz

Industry/Entity Type

marketing

Coding

Coded - Design and coding required

Number of Pages Required

3 page

Requirements
Must have
• impressive design
Nice to have
• im open
Should not have
• open

```html
<!DOCTYPE html>
<html lang="en">
<head>
<meta charset="utf-8">
<title>Complimentary Gift Vouchers</title>
<link href="https://fonts.googleapis.com/css2?family=Plus+Jakarta+Sans:wght@400;500;600;700;800&display=swap" rel="stylesheet">
<style>
  :root {
    --bg: #f7f7f5;
    --ink: #111111;
    --muted: #6b6b6b;
    --card: #ffffff;
    --card-dark: #222222;
    --accent: #2f49f5;
    --icon-a: #c23fd8;
    --icon-b: #e5505c;
    --stat-bg: #f4f4f2;
  }
  * { box-sizing: border-box; margin: 0; padding: 0; }
  html, body { width: 1200px; height: 926px; overflow: hidden; }
  body {
    background: linear-gradient(180deg, var(--bg) 0%, var(--bg) 60%, #ffffff 75%, #ffffff 100%);
    font-family: "Plus Jakarta Sans", sans-serif;
    color: var(--ink);
    position: relative;
  }
  .hero-copy { position: absolute; left: 176px; top: 208px; width: 300px; }
  .hero-title { font-size: 27.5px; font-weight: 500; line-height: 31.5px; letter-spacing: -0.3px; }
  .hero-title strong { font-weight: 800; }
  .hero-note { margin-top: 47px; font-size: 16.5px; line-height: 21px; color: var(--muted); letter-spacing: -0.2px; }
  .cta {
    position: absolute; left: 173px; top: 478px; width: 284px; height: 46px;
    background: var(--accent); color: #fff; border-radius: 13px;
    display: flex; align-items: center; justify-content: center;
    font-size: 13px; font-weight: 700; letter-spacing: -0.2px; text-decoration: none;
  }
  .voucher-grid {
    position: absolute; left: 644px; top: 89px;
    display: grid; grid-template-columns: 163px 163px; grid-auto-rows: 163px;
    column-gap: 15px; row-gap: 15px;
  }
  .voucher {
    background: var(--card); border-radius: 17px; position: relative; padding: 15px;
  }
  .voucher--featured {
    background: var(--card-dark); color: #fff;
    box-shadow: 0 0 14px rgba(160, 90, 255, 0.35);
  }
  .voucher-icon {
    width: 32px; height: 32px; border-radius: 7px;
    background: linear-gradient(90deg, var(--icon-a) 0%, var(--icon-a) 50%, var(--icon-b) 50%, var(--icon-b) 100%);
    display: flex; align-items: center; justify-content: center;
  }
  .voucher-icon svg { width: 18px; height: 18px; }
  .voucher-title {
    position: absolute; left: 15px; top: 79px; font-size: 13px; font-weight: 600; line-height: 15.5px; letter-spacing: -0.1px;
  }
  .voucher-title--two-line { top: 71px; }
  .voucher-desc {
    position: absolute; left: 15px; top: 123px; right: 8px;
    font-size: 10.3px; line-height: 12.6px; color: var(--muted);
  }
  .voucher--featured .voucher-desc { color: #e8e8e8; }
  .stats { position: absolute; top: 725px; left: 170px; display: flex; gap: 19px; }
  .stat {
    width: 121px; height: 116px; border-radius: 14px; padding: 27px 0 0 15px;
    background: var(--stat-bg);
  }
  .stat:first-child { width: 116px; background: linear-gradient(90deg, rgba(244,244,242,0) 0%, var(--stat-bg) 40%); }
  .stat:last-child { width: 115px; background: linear-gradient(90deg, var(--stat-bg) 60%, rgba(244,244,242,0) 100%); }
  .stat-value { font-size: 28px; font-weight: 700; line-height: 30px; letter-spacing: -0.5px; }
  .stat-label { margin-top: 5px; font-size: 10.5px; line-height: 12.6px; color: var(--muted); }
</style>
</head>
<body>
  <section class="hero-copy">
    <h1 class="hero-title">Give away an <strong>unlimited amount</strong> of complimentary gift vouchers</h1>
    <p class="hero-note">(without having to personally pay or fulfill any of them yourself!)</p>
  </section>
  <a class="cta" href="#">SIGN UP FOR A RISK-FREE 14 DAY TRIAL</a>

  <section class="voucher-grid">
    <article class="voucher">
      <div class="voucher-icon"><svg viewBox="0 0 24 24" fill="#fff"><path d="M5 2h14v2h-1v16h2v2H4v-2h2V4H5zM9 6v2h2V6zm4 0v2h2V6zM9 10v2h2v-2zm4 0v2h2v-2zM9 14v2h2v-2zm4 0v2h2v-2zm-2 4v2h2v-2z"/></svg></div>
      <h2 class="voucher-title">Hotel Saving Cards</h2>
      <p class="voucher-desc">Complimentary<br>$100 - $500 Hotel Cards</p>
    </article>
    <article class="voucher voucher--featured">
      <div class="voucher-icon"><svg viewBox="0 0 24 24" fill="#fff"><path d="M11 11C8 6 4 7 2 9c3-1 6 0 8 3-3-1-6 1-7 4 2-2 5-3 8-3zm2 0c3-5 7-4 9-2-3-1-6 0-8 3 3-1 6 1 7 4-2-2-5-3-8-3zM12 10C11 6 8 3 6 3c3 1 5 4 6 7 1-3 3-6 6-7-2 0-5 3-6 7zM11 12h2v10h-2z"/></svg></div>
      <h2 class="voucher-title">Resort Certificates</h2>
      <p class="voucher-desc">Complimentary All Inclusive Vacations</p>
    </article>
    <article class="voucher">
      <div class="voucher-icon"><svg viewBox="0 0 24 24" fill="#fff"><path d="M5 3h14v5a7 7 0 0 1-6 6.9V19h4v2H7v-2h4v-4.1A7 7 0 0 1 5 8zm2 2v3h10V5z"/></svg></div>
      <h2 class="voucher-title">Restaurant Cards</h2>
      <p class="voucher-desc">Complimentary<br>$100 - $500 Dining Cards</p>
    </article>
    <article class="voucher">
      <div class="voucher-icon"><svg viewBox="0 0 24 24" fill="#fff"><path d="M20 3c1 1 0 3-2 5l-3 3 2 9-2 1-4-7-3 3v3l-2 1-1-4-4-1 1-2h3l3-3-7-4 1-2 9 2 3-3c2-2 4-3 5-2z"/></svg></div>
      <h2 class="voucher-title">Airfare Vouchers</h2>
      <p class="voucher-desc">Complimentary<br>Roundtrip Airfare</p>
    </article>
    <article class="voucher">
      <div class="voucher-icon"><svg viewBox="0 0 24 24" fill="#fff"><path d="M11 2v12H3zM13 5l7 9h-7zM2 16h20l-3 5H5z"/></svg></div>
      <h2 class="voucher-title">Cruise Certificates</h2>
      <p class="voucher-desc">Complimentary Cruise Getaways</p>
    </article>
    <article class="voucher">
      <div class="voucher-icon"><svg viewBox="0 0 24 24" fill="#fff"><path d="M9 1h6l1 4a7 7 0 0 1 0 14l-1 4H9l-1-4A7 7 0 0 1 8 5zm3 6a5 5 0 1 0 0 10 5 5 0 0 0 0-10zm-1 1h2v4h3v2h-5z"/></svg></div>
      <h2 class="voucher-title voucher-title--two-line">Smart Device<br>Certificates</h2>
      <p class="voucher-desc">Complimentary Smart Devices</p>
    </article>
  </section>

  <section class="stats">
    <div class="stat"><div class="stat-value">16+</div><div class="stat-label">Years in<br>Business</div></div>
    <div class="stat"><div class="stat-value">17K+</div><div class="stat-label">Clients<br>Enrolled</div></div>
    <div class="stat"><div class="stat-value">11M+</div><div class="stat-label">Certificates<br>Enrolled</div></div>
    <div class="stat"><div class="stat-value">400K</div><div class="stat-label">Incentives<br>Redeemed</div></div>
    <div class="stat"><div class="stat-value">$20M+</div><div class="stat-label">In Savings for<br>Redeemers</div></div>
    <div class="stat"><div class="stat-value">100’s</div><div class="stat-label">of Reviews &amp;<br>Testimonials</div></div>
  </section>
</body>
</html>
```